Morden, Creative, Unique, Independent Wine Shop

1. We are a brand new wine shop located in Melbourne Australia, we have our logo already, simply use the logo to design a business card.
2. I have uploaded our logo in two versions, with or without shadow, any of them is acceptable.
3. Make it as creative and unique as possible, no limitation of shape, color combination, geometry pattern, fonts, composing etc.
3. Info on the card:
- Brambleford Wine Cellar (Not very necessary if logo is obviously shown)
- 42 Ferncastle Steet, Hampton, Victoria, Australia 3188
- +61 3 9018 4637
- www.bramblefordwinecellar.com.au
- bramblefordwinecellar@mailvista.com
- Additional icons: Google, Instagram, Facebook, Twitter
4. Once again, forget it is a commercial card, make it special.

```html
<!DOCTYPE html>
<html lang="en">
<head>
<meta charset="utf-8">
<title>Brambleford Wine Cellar – Business Card</title>
<link rel="stylesheet" href="https://fonts.googleapis.com/css2?family=Roboto:wght@400;500&display=swap">
<style>
  :root {
    --backdrop: #cbcbcb;
    --paper: #ffffff;
    --wine: #84161a;
    --wine-text: #7d1418;
    --ink-soft: #666666;
    --rule: #9a9a9a;
    --shadow: rgba(0, 0, 0, 0.28);
  }
  * { margin: 0; padding: 0; box-sizing: border-box; }
  html, body {
    width: 1200px;
    height: 1200px;
    overflow: hidden;
    background: var(--backdrop);
    font-family: "Roboto", Arial, sans-serif;
  }
  .canvas { position: relative; width: 1200px; height: 1200px; }

  .card {
    position: absolute;
    left: 204px;
    width: 786px;
    height: 450px;
    box-shadow: 0 6px 14px var(--shadow);
    overflow: hidden;
  }
  .card--front { top: 132px; background: var(--paper); }
  .card--back { top: 620px; background: var(--wine); }

  .front__band {
    position: absolute;
    left: 0; right: 0; bottom: 0;
    height: 17px;
    background: var(--wine);
  }

  .brand {
    position: absolute;
    display: flex;
    align-items: center;
  }
  .brand__mark { border-radius: 50%; flex: none; }
  .brand__name {
    font-weight: 400;
    line-height: 1.05;
    letter-spacing: 0.02em;
  }

  .front__brand { left: 96px; top: 166px; gap: 16px; }
  .front__brand .brand__mark { width: 54px; height: 54px; background: var(--wine); }
  .front__brand .brand__name { font-size: 30px; color: var(--wine-text); }

  .front__divider {
    position: absolute;
    left: 393px;
    top: 136px;
    width: 1.5px;
    height: 177px;
    background: var(--rule);
  }

  .contact {
    position: absolute;
    left: 426px;
    top: 130px;
    color: var(--ink-soft);
  }
  .contact__title {
    font-size: 23px;
    font-weight: 500;
    color: var(--wine-text);
    margin-bottom: 14px;
  }
  .contact__address {
    font-size: 17.5px;
    line-height: 24px;
    font-style: normal;
    margin-bottom: 12px;
  }
  .contact__list { list-style: none; }
  .contact__item {
    display: flex;
    align-items: center;
    gap: 9px;
    font-size: 17.5px;
    line-height: 30px;
  }
  .contact__icon { width: 13px; height: 13px; flex: none; fill: var(--wine); }

  .back__brand {
    left: 0; right: 0; top: 110px;
    justify-content: center;
    gap: 24px;
  }
  .back__brand .brand__mark { width: 96px; height: 96px; background: var(--paper); }
  .back__brand .brand__name { font-size: 48px; color: var(--paper); }

  .social {
    position: absolute;
    left: 0; right: 0; top: 380px;
    display: flex;
    justify-content: center;
    gap: 8px;
    list-style: none;
  }
  .social__dot {
    width: 26px;
    height: 26px;
    border-radius: 50%;
    background: var(--paper);
  }
</style>
</head>
<body>
<main class="canvas">

  <section class="card card--front" aria-label="Business card front">
    <div class="brand front__brand">
      <span class="brand__mark"></span>
      <span class="brand__name">Brambleford<br>Wine Cellar</span>
    </div>

    <div class="front__divider"></div>

    <div class="contact">
      <h1 class="contact__title">Brambleford Wine Cellar</h1>
      <address class="contact__address">42 Ferncastle Steet, Hampton,<br>Victoria, Australia 3188</address>
      <ul class="contact__list">
        <li class="contact__item">
          <svg class="contact__icon" viewBox="0 0 24 24" aria-hidden="true"><path d="M6.6 10.8a15 15 0 0 0 6.6 6.6l2.2-2.2c.3-.3.7-.4 1-.2 1.1.4 2.3.6 3.6.6.6 0 1 .4 1 1V20c0 .6-.4 1-1 1A17 17 0 0 1 3 4c0-.6.4-1 1-1h3.5c.6 0 1 .4 1 1 0 1.3.2 2.5.6 3.6.1.3 0 .7-.2 1z"/></svg>
          <span>+61 3 9018 4637</span>
        </li>
        <li class="contact__item">
          <svg class="contact__icon" viewBox="0 0 24 24" aria-hidden="true"><path d="M2 5h20v14H2z M4 7v1l8 5 8-5V7l-8 5z" fill-rule="evenodd"/></svg>
          <span>bramblefordwinecellar@mailvista.com</span>
        </li>
        <li class="contact__item">
          <svg class="contact__icon" viewBox="0 0 24 24" aria-hidden="true"><circle cx="12" cy="12" r="10"/></svg>
          <span>www.bramblefordwinecellar.com.au</span>
        </li>
      </ul>
    </div>

    <div class="front__band"></div>
  </section>

  <section class="card card--back" aria-label="Business card back">
    <div class="brand back__brand">
      <span class="brand__mark"></span>
      <span class="brand__name">Brambleford<br>Wine Cellar</span>
    </div>
    <ul class="social" aria-label="Social media links">
      <li class="social__dot"></li>
      <li class="social__dot"></li>
      <li class="social__dot"></li>
      <li class="social__dot"></li>
    </ul>
  </section>

</main>
</body>
</html>
```